'Tarvel' a financial/crypto-currency exchange in the middle east

On the card we need 1) Name 2) title 3) email address 4) phone number using the same colors and theme as the logo. On one side we just want the logo and we want the whole card to be in blue (same blue as logo) with the logo in the back being white.
Industry/Entity Type
Financial

```html
<!DOCTYPE html>
<html lang="en">
<head>
<meta charset="utf-8">
<title>Tarvel Business Card</title>
<link rel="stylesheet" href="https://fonts.googleapis.com/css2?family=Nunito+Sans:wght@400;700;800&display=swap">
<style>
  :root {
    --brand-blue: #1890cc;
    --ink: #111418;
    --paper: #ffffff;
    --backdrop: #8c8c8c;
    --backdrop-light: #bdbdbd;
  }
  * { box-sizing: border-box; margin: 0; padding: 0; }
  html, body {
    width: 1200px; height: 1200px; overflow: hidden;
  }
  body {
    background: radial-gradient(ellipse at 50% 45%, var(--backdrop-light), var(--backdrop) 75%);
    font-family: "Nunito Sans", sans-serif;
    color: var(--ink);
    position: relative;
  }
  .card {
    position: absolute;
    left: 160px;
    width: 880px;
    height: 503px;
    border-radius: 18px;
    box-shadow: 0 10px 26px rgba(0,0,0,0.35);
    overflow: hidden;
  }
  .card--front { top: 60px; background: var(--paper); }
  .card--back  { top: 637px; background: var(--brand-blue); }

  .brand-block {
    position: absolute;
    left: 0; top: 0;
    width: 412px; height: 100%;
    display: flex; flex-direction: column;
    align-items: center; justify-content: center;
    gap: 22px;
  }
  .brand-dot {
    width: 190px; height: 190px; border-radius: 50%;
    background: var(--brand-blue);
  }
  .brand-name {
    font-weight: 800;
    font-size: 64px;
    letter-spacing: 1px;
    color: var(--brand-blue);
    line-height: 1;
  }
  .divider {
    position: absolute;
    left: 412px; top: 70px;
    width: 2px; height: 363px;
    background: var(--brand-blue);
  }
  .contact {
    position: absolute;
    left: 470px; top: 82px;
  }
  .contact__name {
    font-weight: 800; font-size: 44px; line-height: 1.1;
  }
  .contact__title {
    color: var(--brand-blue); font-size: 29px; margin-top: 4px;
  }
  .contact__list { list-style: none; margin-top: 28px; }
  .contact__list li {
    display: flex; align-items: center; gap: 14px;
    font-size: 30px; line-height: 46px;
  }
  .contact__list svg { width: 26px; height: 26px; flex: none; }
  .contact__address {
    font-size: 30px; line-height: 44px; margin-top: 22px;
  }

  .back-brand {
    position: absolute; inset: 0;
    display: flex; align-items: center; justify-content: center;
    gap: 34px;
  }
  .back-brand__ring {
    width: 190px; height: 190px; border-radius: 50%;
    border: 10px solid var(--paper);
  }
  .back-brand__name {
    font-weight: 800; font-size: 118px; color: var(--paper);
    letter-spacing: 2px; line-height: 1;
  }
</style>
</head>
<body>

<section class="card card--front" aria-label="Card front">
  <div class="brand-block">
    <div class="brand-dot"></div>
    <div class="brand-name">Tarvel</div>
  </div>
  <div class="divider"></div>
  <div class="contact">
    <h1 class="contact__name">John Smith</h1>
    <p class="contact__title">Director</p>
    <ul class="contact__list">
      <li>
        <svg viewBox="0 0 24 24" fill="none" stroke="#777" stroke-width="1.4"><rect x="6" y="1.5" width="12" height="21" rx="2"/><line x1="6" y1="18" x2="18" y2="18"/><line x1="6" y1="5" x2="18" y2="5"/></svg>
        (000) 000-1000
      </li>
      <li>
        <svg viewBox="0 0 24 24" fill="none" stroke="#777" stroke-width="1.4"><path d="M5 2.5l4 4-2.5 3a13 13 0 0 0 8 8l3-2.5 4 4-3 3C10 21 3 14 2 5.5z"/></svg>
        (000) 000-2000
      </li>
      <li>
        <svg viewBox="0 0 24 24" fill="none" stroke="#777" stroke-width="1.4"><rect x="2" y="5" width="20" height="14"/><path d="M2 5l10 8 10-8M2 19l7.5-7M22 19l-7.5-7"/></svg>
        name@email.com
      </li>
      <li>
        <svg viewBox="0 0 24 24" fill="none" stroke="#777" stroke-width="1.4"><path d="M2 12L12 3l10 9M5 10v11h5v-6h4v6h5V10"/></svg>
        www.domain.com
      </li>
    </ul>
    <p class="contact__address">Unit, Street,<br>City, State, Zip Code</p>
  </div>
</section>

<section class="card card--back" aria-label="Card back">
  <div class="back-brand">
    <div class="back-brand__ring"></div>
    <div class="back-brand__name">Tarvel</div>
  </div>
</section>

</body>
</html>
```